Business card design needed

We do excavation, cartage and contracting
I would quote like to have a picture of my digger as the whole back ground and the words on top. If that looks any good
Otherwise please feel free to come up with any other cool options

Cheers Marc

Industry/Entity Type

Business

Contact Information for Business Card

KRV Contracting
Excavation, Cartage, Contracting
Marcus Pellow
www.krv.co.nz
027 584 612
marc@krv.co.nz

```html
<!DOCTYPE html>
<html lang="en">
<head>
<meta charset="utf-8">
<title>KRV Contracting – Business Card</title>
<link rel="stylesheet" href="https://fonts.googleapis.com/css2?family=Fira+Sans:wght@400&display=swap">
<style>
  :root {
    --page-bg: #1b1b1b;
    --green-light: #2d6b34;
    --green-dark: #214b26;
    --blue-light: #10465e;
    --blue-dark: #0a2838;
    --ink: #ffffff;
  }
  html, body {
    margin: 0;
    padding: 0;
    width: 1200px;
    height: 830px;
    overflow: hidden;
    background: var(--page-bg);
  }
  .canvas {
    position: relative;
    width: 1200px;
    height: 830px;
  }
  .card {
    position: absolute;
    left: 170px;
    top: 173px;
    width: 860px;
    height: 464px;
    display: flex;
    font-family: "Fira Sans", Arial, sans-serif;
    color: var(--ink);
    box-shadow: 0 12px 40px rgba(0, 0, 0, 0.6);
  }
  .card__brand {
    width: 430px;
    height: 100%;
    background: linear-gradient(180deg, var(--green-light) 0%, var(--green-dark) 100%);
    display: flex;
    align-items: center;
    justify-content: center;
  }
  .brand-name {
    font-size: 92px;
    font-weight: 400;
    letter-spacing: 2px;
    line-height: 1;
    margin: 0;
    color: var(--ink);
  }
  .card__details {
    width: 430px;
    height: 100%;
    background: radial-gradient(ellipse at 20% 0%, var(--blue-light) 0%, var(--blue-dark) 90%);
    box-sizing: border-box;
    padding: 112px 0 0 53px;
  }
  .details-list {
    list-style: none;
    margin: 0;
    padding: 0;
    font-size: 25px;
    line-height: 40px;
    font-weight: 400;
  }
</style>
</head>
<body>
  <main class="canvas">
    <section class="card">
      <div class="card__brand">
        <p class="brand-name">KRV</p>
      </div>
      <div class="card__details">
        <ul class="details-list">
          <li>KRV Contracting Excavation</li>
          <li>Cartage</li>
          <li>Contracting Marcus Pellow</li>
          <li>www.krv.co.nz</li>
          <li>027 584 612</li>
          <li>marc@krv.co.nz</li>
        </ul>
      </div>
    </section>
  </main>
</body>
</html>
```